Verpackungsdesign für hochwertiges Haarparfum
Zielgruppe
Tovel's Method ist eine israelische Firma, die hochqualitative Haarprodukte und Haar Tools verkauft. Unsere Zielgruppe sind Frauen, die viel in Ihr Aussehen investieren und auf Ihr Äußeres sehr Wert legen.
Aufgabenstellung
Wir suchen nach einem Design für unsere zwei neuen Haarparfums. Es sollte teuer aussehen und das Design sollte modern und simpel sein. Die Flachen sind mit Milchglas und das Design wird auf die Flaschen gedruckt. Das Design muss komplett in Englischer Sprache sein.
Die Masse sind:
Höhe 7,7 cm
Umfang 11 cm
Es wird zwei Düfte geben.
1. The Nordic : Deckel wird Silber glänzend
2. The Celtic: Deckel wird Silber matt
Informationen die auf der Flasche sein sollten:
1. Firmen Logo (wird angehängt)
2. Name des Parfüms (The Nordic or the Celtic)
3. Longlasting Hair Fragrance
4. 30 ml
5. Includes essential hair vitamins and minerals
6. Alcohol and salt free

```html
<!DOCTYPE html>
<html lang="de">
<head>
<meta charset="utf-8">
<title>Tovel's Method – Haarparfum Etiketten</title>
<link href="https://fonts.googleapis.com/css2?family=Montserrat:wght@200;300;400&display=swap" rel="stylesheet">
<style>
  :root {
    --paper: #ffffff;
    --ink: #111111;
    --gold: #c9a227;
    --gold-light: #ecd68a;
    --grey-text: #7a7a7a;
    --frame: #222222;
    --silver-dark: #8e9296;
    --silver-mid: #c9ccd0;
    --silver-light: #f6f7f8;
    --frost-dark: #cfd1d3;
    --frost-light: #eef0f1;
  }
  * { box-sizing: border-box; margin: 0; padding: 0; }
  html, body {
    width: 684px; height: 1200px; overflow: hidden;
    background: var(--paper);
    font-family: "Montserrat", Arial, sans-serif;
    color: var(--ink);
  }
  .sheet { position: relative; width: 684px; height: 1200px; }

  /* flat label artwork */
  .label {
    position: absolute; width: 268px; height: 375px;
    border: 1px solid var(--frame); background: var(--paper);
  }
  .brand {
    position: absolute; left: 50%; top: 52px; transform: translateX(-50%);
    display: flex; align-items: center; gap: 6px;
  }
  .brand-square { width: 11px; height: 11px; border: 1px solid #333; }
  .brand-name {
    font-weight: 300; font-size: 12px; letter-spacing: 2px;
    text-transform: uppercase; color: #333; white-space: nowrap;
  }
  .scent-name {
    position: absolute; left: 0; right: 0; top: 94px; text-align: center;
    font-weight: 200; font-size: 60px; line-height: 1; letter-spacing: 1px;
    color: var(--gold);
  }
  .tagline {
    position: absolute; left: 0; right: 0; top: 155px; text-align: center;
    font-weight: 300; font-size: 8.5px; letter-spacing: 3.4px; color: #555;
  }
  .artwork {
    position: absolute; left: 10px; right: 10px; top: 168px; height: 140px;
    background: radial-gradient(ellipse at center, var(--gold-light) 0%, #f7efd2 55%, var(--paper) 100%);
  }
  .facts {
    position: absolute; left: 0; right: 0; top: 320px; text-align: center;
    font-weight: 300; font-size: 7.4px; line-height: 11.5px; color: var(--grey-text);
  }

  .option-title {
    position: absolute; font-weight: 400; font-size: 16px; letter-spacing: .3px;
  }

  /* bottle mockups */
  .bottle { position: absolute; width: 96px; height: 325px; }
  .bottle-cap {
    position: absolute; left: 14px; width: 68px; top: 0; height: 112px;
    border-radius: 4px 4px 0 0;
    background: linear-gradient(90deg, var(--silver-dark) 0%, var(--silver-light) 18%, var(--silver-mid) 35%, #7d8185 50%, var(--silver-light) 68%, var(--silver-mid) 85%, var(--silver-dark) 100%);
  }
  .bottle-body {
    position: absolute; left: 0; right: 0; top: 104px; bottom: 0;
    border-radius: 16px 16px 36px 36px;
    background: linear-gradient(90deg, var(--frost-dark), var(--frost-light) 45%, var(--frost-dark));
    overflow: hidden;
  }
  .bottle-print {
    position: absolute; left: 0; right: 0; top: 32px; height: 168px;
    text-align: center;
  }
  .bottle-print--sticker { background: var(--paper); top: 30px; height: 166px; }
  .mini-brand {
    display: inline-flex; align-items: center; gap: 2px; margin-top: 16px;
    font-weight: 400; font-size: 4.6px; letter-spacing: .6px; color: #333; white-space: nowrap;
  }
  .mini-brand i { width: 5px; height: 5px; border: .6px solid #333; }
  .mini-name {
    font-weight: 200; font-size: 22px; line-height: 1; letter-spacing: .3px;
    color: var(--gold); margin-top: 4px;
  }
  .mini-tagline { font-weight: 300; font-size: 3.4px; letter-spacing: 1.1px; color: #555; margin-top: 2px; }
  .mini-art {
    height: 56px; margin: 4px 2px 0;
    background: radial-gradient(ellipse at center, var(--gold-light) 0%, rgba(236,214,138,.35) 55%, rgba(255,255,255,0) 100%);
  }
  .mini-facts { font-weight: 300; font-size: 3px; line-height: 4.6px; color: #666; margin-top: 3px; }

  .notes {
    position: absolute; left: 43px; font-size: 16.5px; line-height: 20.5px; font-weight: 400;
  }
  .divider {
    position: absolute; left: 49px; width: 593px; top: 581px; height: 2px; background: var(--ink);
  }
</style>
</head>
<body>
<main class="sheet">

  <section class="label" style="left:41px; top:62px;">
    <div class="brand"><span class="brand-square"></span><span class="brand-name">Tovel's Method</span></div>
    <h2 class="scent-name">NORDIC</h2>
    <p class="tagline">LONGLASTING HAIR FRAGRANCE</p>
    <div class="artwork" role="img" aria-label="Gold line illustration of a woman in profile with flowing hair"></div>
    <p class="facts">INCLUDES ESSENTIAL HAIR VITAMINS AND MINERALS<br>ALCOHOL AND SALT FREE<br>30 ML</p>
  </section>
  <p class="option-title" style="left:392px; top:44px;">1 OPTION</p>
  <p class="option-title" style="left:543px; top:44px;">2 OPTION</p>

  <div class="bottle" style="left:378px; top:98px;">
    <div class="bottle-body">
      <div class="bottle-print">
        <span class="mini-brand"><i></i>TOVEL'S METHOD</span>
        <p class="mini-name">NORDIC</p>
        <p class="mini-tagline">LONGLASTING HAIR FRAGRANCE</p>
        <div class="mini-art" role="img" aria-label="Gold line illustration of a woman with flowing hair"></div>
        <p class="mini-facts">INCLUDES ESSENTIAL HAIR VITAMINS AND MINERALS<br>ALCOHOL AND SALT FREE<br>30 ML</p>
      </div>
    </div>
    <div class="bottle-cap"></div>
  </div>
  <div class="bottle" style="left:532px; top:95px;">
    <div class="bottle-body">
      <div class="bottle-print bottle-print--sticker">
        <span class="mini-brand"><i></i>TOVEL'S METHOD</span>
        <p class="mini-name">NORDIC</p>
        <p class="mini-tagline">LONGLASTING HAIR FRAGRANCE</p>
        <div class="mini-art" role="img" aria-label="Gold line illustration of a woman with flowing hair"></div>
        <p class="mini-facts">INCLUDES ESSENTIAL HAIR VITAMINS AND MINERALS<br>ALCOHOL AND SALT FREE<br>30 ML</p>
      </div>
    </div>
    <div class="bottle-cap"></div>
  </div>

  <p class="notes" style="top:464px;">1 OPTION<br>DAS ETIKETT IST AUF DER FLASCHE SELBST AUFGEDRUCKT<br>2 VARIANTE<br>ETIKETT AUF WEIßEM HINTERGRUND</p>

  <div class="divider"></div>

  <section class="label" style="left:41px; top:630px; width:269px; height:377px;">
    <div class="brand"><span class="brand-square"></span><span class="brand-name">Tovel's Method</span></div>
    <h2 class="scent-name">CELTIC</h2>
    <p class="tagline">LONGLASTING HAIR FRAGRANCE</p>
    <div class="artwork" role="img" aria-label="Gold line illustration of a woman in profile with flowing hair"></div>
    <p class="facts">INCLUDES ESSENTIAL HAIR VITAMINS AND MINERALS<br>ALCOHOL AND SALT FREE<br>30 ML</p>
  </section>
  <p class="option-title" style="left:392px; top:623px;">1 OPTION</p>
  <p class="option-title" style="left:543px; top:623px;">2 OPTION</p>

  <div class="bottle" style="left:378px; top:673px;">
    <div class="bottle-body">
      <div class="bottle-print">
        <span class="mini-brand"><i></i>TOVEL'S METHOD</span>
        <p class="mini-name">CELTIC</p>
        <p class="mini-tagline">LONGLASTING HAIR FRAGRANCE</p>
        <div class="mini-art" role="img" aria-label="Gold line illustration of a woman with flowing hair"></div>
        <p class="mini-facts">INCLUDES ESSENTIAL HAIR VITAMINS AND MINERALS<br>ALCOHOL AND SALT FREE<br>30 ML</p>
      </div>
    </div>
    <div class="bottle-cap"></div>
  </div>
  <div class="bottle" style="left:532px; top:670px;">
    <div class="bottle-body">
      <div class="bottle-print bottle-print--sticker">
        <span class="mini-brand"><i></i>TOVEL'S METHOD</span>
        <p class="mini-name">CELTIC</p>
        <p class="mini-tagline">LONGLASTING HAIR FRAGRANCE</p>
        <div class="mini-art" role="img" aria-label="Gold line illustration of a woman with flowing hair"></div>
        <p class="mini-facts">INCLUDES ESSENTIAL HAIR VITAMINS AND MINERALS<br>ALCOHOL AND SALT FREE<br>30 ML</p>
      </div>
    </div>
    <div class="bottle-cap"></div>
  </div>

  <p class="notes" style="top:1027px;">1 OPTION<br>DAS ETIKETT IST AUF DER FLASCHE SELBST AUFGEDRUCKT<br>2 VARIANTE<br>ETIKETT AUF WEIßEM HINTERGRUND</p>

</main>
</body>
</html>
```